Company Website

We require an online clothing store website for construction workwear.
It needs to be easy to read, user friendly, easy to navigate purchasing.
We are after designs incorporating our recently design logo, and colour combinations black white and orange (same as the company logo). Needs to highlight quality, safety and products. Any ideas around highlighting branding are welcome.

Target Market(s)

Construction workers and businesses.

Industry/Entity Type

Construction

Coding

Coded - Design and coding required

Number of Pages Required

5+ page

Colors
EE7325
F08F49
F5BC92
FAE3D3
FDF4ED

Requirements
Must have
• Include all pictures, prices and details of the products we sell. See PDF uploaded to brief.
Nice to have
• Simple access to purchase items. Easy to navigate website layout.

```html
<!DOCTYPE html>
<html lang="en">
<head>
<meta charset="utf-8">
<title>Ironline Workgear – Construction Workwear</title>
<link href="https://fonts.googleapis.com/css2?family=Poppins:wght@300;400;500;600;700;800&display=swap" rel="stylesheet">
<style>
:root{
  --orange:#f25c05;
  --orange-soft:#F08F49;
  --peach:#F5BC92;
  --cream:#FAE3D3;
  --ink:#111;
  --grey:#8a8a8a;
  --page:#f6f6f6;
  --white:#fff;
  --green:#3a8a3a;
}
*{box-sizing:border-box;margin:0;padding:0}
html,body{width:1200px;height:3827px;overflow:hidden}
body{font-family:"Poppins",sans-serif;color:var(--ink);background:var(--page);position:relative}
.abs{position:absolute}
.wordmark{font-family:"Poppins",sans-serif;font-weight:700;color:var(--orange);letter-spacing:3px;line-height:1}
.wordmark small{display:block;font-size:10px;letter-spacing:6px;color:var(--ink);font-weight:600;margin-top:4px;text-align:right}

/* header */
.header{left:0;top:0;width:1200px;height:88px;background:var(--white)}
.search{left:417px;top:27px;width:476px;height:45px;border:1px solid #ccc;display:flex}
.search span{flex:1;font-size:10px;color:#777;padding:15px 24px}
.search b{width:74px;background:var(--ink);display:flex;align-items:center;justify-content:center}
.login{left:1100px;top:36px;font-size:11px;font-weight:500}
.nav{left:0;top:88px;width:1200px;height:56px;background:var(--orange);display:flex;align-items:center;color:var(--white);font-size:19px;font-weight:500}
.nav a{margin-left:38px;color:inherit;text-decoration:none}
.nav a:first-child{margin-left:38px}
.nav .cur{margin-left:auto;margin-right:24px}

/* hero */
.hero{left:0;top:144px;width:1200px;height:601px;background:linear-gradient(160deg,#5f6d7c 0%,#8a8f8f 35%,#6b5e4c 70%,#3f3428 100%)}
.hero h1{left:44px;top:95px;font-size:74px;font-weight:800;color:var(--white);line-height:92px}
.hero p{left:50px;top:292px;width:560px;font-size:19px;color:var(--white);line-height:24px;font-weight:400}
.btn{display:flex;align-items:center;justify-content:center;gap:10px;color:var(--white);font-size:17px;font-weight:500}
.btn-dark{background:var(--ink)}
.btn-orange{background:var(--orange)}

/* features */
.features{left:195px;top:686px;width:833px;height:164px;background:var(--white);display:flex;align-items:center;justify-content:space-around;padding:0 30px}
.feature{display:flex;gap:14px;align-items:center}
.feature h4{font-size:17px;font-weight:600}
.feature p{font-size:10px;color:#aaa;line-height:12px;width:150px}

/* promos */
.promo{background:linear-gradient(120deg,#4c4a48,#7a6f62 50%,#3d3b39)}
.promo-text{position:absolute;right:52px;text-align:right;color:var(--white)}
.promo-text h3{font-weight:700;line-height:1}
.promo-text p{font-size:13px;margin-top:16px}
.promo-text .btn{margin-left:auto;margin-top:22px;width:164px;height:38px;font-size:18px}

.section-title{width:1200px;text-align:center;font-size:44px;font-weight:700;letter-spacing:1px}
.section-title em{font-style:normal;color:var(--orange);margin-left:12px}

/* products */
.product{width:247px}
.product .img{height:282px;background:var(--white);position:relative}
.product .img i{position:absolute;left:50%;top:50%;transform:translate(-50%,-50%);width:150px;height:190px;border-radius:12px}
.badge{position:absolute;left:8px;top:8px;width:46px;height:46px;border-radius:50%;color:var(--white);font-size:11px;font-weight:600;display:flex;align-items:center;justify-content:center}
.product h5{font-size:12px;font-weight:500;margin-top:14px;line-height:18px;width:220px}
.product .cat{font-size:11px;color:#aaa;margin-top:4px}
.product .price{font-size:12px;color:var(--orange);margin-top:8px}
.rating{position:absolute;right:0;top:296px;font-size:11px}

/* brands */
.brands-band{left:0;top:2268px;width:1200px;height:560px;background:var(--white)}
.brand{font-size:26px;font-weight:700;color:#333}
.arrow-dot{width:28px;height:28px;border-radius:50%;background:var(--orange)}

/* news */
.news-card{width:258px;height:365px;background:linear-gradient(160deg,#8a6a50,#4e3a2c)}
.date{position:absolute;left:12px;top:12px;width:44px;height:52px;background:var(--white);text-align:center;font-size:18px;line-height:22px;padding-top:6px}
.date small{display:block;font-size:9px;line-height:12px}
.news-meta{position:absolute;left:0;bottom:20px;width:100%;text-align:center;color:var(--white)}
.tag{display:inline-block;background:var(--orange);font-size:8px;font-weight:600;padding:3px 10px}
.news-meta h5{font-size:16px;font-weight:600;line-height:24px;margin-top:8px;padding:0 20px}
.news-meta small{font-size:10px;color:#ddd;display:block;margin-top:6px}

/* newsletter */
.newsletter{left:0;top:3272px;width:1200px;height:198px;background:var(--orange)}
.newsletter h2{left:58px;top:50px;font-size:43px;font-weight:700;color:var(--white);line-height:52px}
.newsletter .field{left:430px;top:78px;width:235px;height:40px;background:var(--white);font-size:16px;padding:9px 22px;color:#333}
.newsletter .btn{left:682px;top:78px;width:234px;height:40px}

/* footer */
.footer{left:0;top:3470px;width:1200px;height:357px;background:#0a0a0a;color:var(--white)}
.footer h6{font-size:13px;font-weight:600;letter-spacing:.5px}
.footer ul{list-style:none;font-size:12px;color:#bbb;line-height:33px;margin-top:8px}
.footer .about{font-size:11px;color:#ccc;line-height:21px}
.contact{font-size:11px;color:#ccc;line-height:28px}
.post{display:flex;gap:12px;font-size:12px;font-weight:600;line-height:17px}
.post i{width:73px;height:56px;flex:none;background:linear-gradient(135deg,#c86a3a,#6a4c3a)}
.post small{display:block;font-size:10px;font-weight:400;color:#aaa;margin-top:6px}
.pay{width:34px;height:22px;background:var(--white);border-radius:2px;font-size:6px;color:#333;display:flex;align-items:center;justify-content:center;font-weight:600}
</style>
</head>
<body>

<header class="header abs">
  <div class="abs wordmark" style="left:37px;top:24px;font-size:36px">IRONLINE<small>WORKGEAR</small></div>
  <div class="search abs"><span>What are you looking for.....</span><b><svg width="22" height="22" viewBox="0 0 22 22"><circle cx="9" cy="9" r="7" fill="none" stroke="#f25c05" stroke-width="2.5"/><path d="M14 14l6 6" stroke="#f25c05" stroke-width="2.5"/></svg></b></div>
  <svg class="abs" style="left:1045px;top:33px" width="36" height="30" viewBox="0 0 36 30"><path d="M4 10h20l-2 18H6z" fill="none" stroke="#f25c05" stroke-width="2"/><path d="M9 10a5 5 0 0 1 10 0" fill="none" stroke="#f25c05" stroke-width="2"/><circle cx="28" cy="7" r="7" fill="#111"/><text x="28" y="10" fill="#fff" font-size="8" text-anchor="middle" font-family="Poppins">0</text></svg>
  <svg class="abs" style="left:1100px;top:33px" width="28" height="28" viewBox="0 0 28 28"><circle cx="14" cy="14" r="12" fill="none" stroke="#f25c05" stroke-width="2"/><circle cx="14" cy="11" r="4" fill="none" stroke="#f25c05" stroke-width="2"/><path d="M7 22a8 8 0 0 1 14 0" fill="none" stroke="#f25c05" stroke-width="2"/></svg>
  <div class="login abs" style="left:1132px">Login</div>
</header>

<nav class="nav abs">
  <a>HOME</a><a>ABOUT</a><a>SHOP</a><a>CATEGORIES</a><a style="margin-left:54px">NEW ARRIVALS</a><a style="margin-left:56px">BLOG</a>
  <a class="cur">US DOLLAR ▾</a>
</nav>

<section class="hero abs" role="img" aria-label="Construction worker in hard hat and hi-vis vest on a building site with cranes">
  <h1 class="abs">GEAR UP<br>FOR SPRNIG</h1>
  <p class="abs">Lorem ipsum dolor sit amet, consectetur adipiscing elit. Ut elit tellus, luctus nec ullamcorper mattis, pulvinar dapibus leo.</p>
  <div class="btn btn-dark abs" style="left:50px;top:379px;width:181px;height:45px">NEW ARRIVALS <span>⟶</span></div>
  <div class="btn btn-orange abs" style="left:258px;top:379px;width:181px;height:45px">SHOP NOW <span>⟶</span></div>
</section>

<section class="features abs">
  <div class="feature">
    <svg width="72" height="80" viewBox="0 0 72 80"><circle cx="36" cy="48" r="26" fill="none" stroke="#f25c05" stroke-width="2.5"/><circle cx="36" cy="48" r="16" fill="none" stroke="#f25c05" stroke-width="2"/><path d="M14 12l3 6 6 1-4 4 1 6-6-3-6 3 1-6-4-4 6-1zM36 4l3 6 6 1-4 4 1 6-6-3-6 3 1-6-4-4 6-1zM58 12l3 6 6 1-4 4 1 6-6-3-6 3 1-6-4-4 6-1z" fill="none" stroke="#f25c05" stroke-width="1.8"/></svg>
    <div><h4>QUALITY</h4><p>Lorem ipsum dolor sit amet Ut elit tellus, luctus nec</p></div>
  </div>
  <div class="feature">
    <svg width="70" height="70" viewBox="0 0 70 70"><path d="M18 26a17 17 0 0 1 34 0z" fill="none" stroke="#f25c05" stroke-width="2.5"/><path d="M14 26h42" stroke="#f25c05" stroke-width="2.5"/><path d="M22 30a13 13 0 0 0 26 0" fill="none" stroke="#f25c05" stroke-width="2.5"/><path d="M8 66c2-16 12-20 27-20s25 4 27 20" fill="none" stroke="#f25c05" stroke-width="2.5"/><path d="M48 46l10 3v8c0 5-5 8-10 10-5-2-10-5-10-10v-8z" fill="#fff" stroke="#f25c05" stroke-width="2.5"/></svg>
    <div><h4>SAFETY</h4><p>Lorem ipsum dolor sit amet Ut elit tellus, luctus nec</p></div>
  </div>
  <div class="feature">
    <svg width="80" height="64" viewBox="0 0 80 64"><path d="M4 12l10-8h8v8a8 8 0 0 0 16 0V4h8l10 8v48H4z" fill="none" stroke="#f25c05" stroke-width="2.5"/><path d="M12 30h10v10H12zM36 30h10v10H36z" fill="none" stroke="#f25c05" stroke-width="2"/><path d="M56 60h22v-4H56zM60 56a7 7 0 0 1 14 0" fill="none" stroke="#f25c05" stroke-width="2.5"/></svg>
    <div><h4>PRODUCTS</h4><p>Lorem ipsum dolor sit amet Ut elit tellus, luctus nec</p></div>
  </div>
</section>

<section class="promo abs" style="left:52px;top:898px;width:623px;height:285px" role="img" aria-label="Smiling workers in orange hi-vis vests in a warehouse">
  <div class="promo-text" style="top:66px;right:52px"><h3 style="font-size:46px">New Arrivals</h3><p>Discount up to 20% for Latest Parts</p><div class="btn btn-orange">SHOP NOW</div></div>
</section>
<section class="promo abs" style="left:713px;top:898px;width:432px;height:285px" role="img" aria-label="Two workers in hard hats and safety vests">
  <div class="promo-text" style="top:58px;right:28px"><h3 style="font-size:44px">ON SALE</h3><p>Discount up to 20% for Latest Parts</p><div class="btn btn-orange">SHOP NOW</div></div>
</section>

<h2 class="section-title abs" style="top:1290px">RECENT<em>PRODUCTS</em></h2>

<!-- product row 1 -->
<div class="product abs" style="left:83px;top:1411px"><div class="img" role="img" aria-label="Hi-vis polo shirts in yellow and orange"><i style="background:linear-gradient(90deg,#c9f05a 50%,#f27a1a 50%)"></i></div><h5>HI- VIS L/S POLO</h5><div class="cat">Furniture</div><div class="price">$23.00</div></div>
<div class="product abs" style="left:350px;top:1411px"><div class="img" role="img" aria-label="Navy work pants with reflective tape"><i style="background:#1f2d5a;width:90px"></i><span class="badge" style="background:#e53512">HOT</span></div><span class="rating">4 <span style="color:#f5b400">★</span></span><h5>HI-VIS NAVY PANTS - DOUBLE HOOP</h5><div class="cat">Accessories</div><div class="price">$47.00</div></div>
<div class="product abs" style="left:616px;top:1411px"><div class="img" role="img" aria-label="Orange reflective vented shirt"><i style="background:#f37a1e;width:190px"></i><span class="badge" style="background:var(--green)">NEW</span></div><h5>MENS L/S REFLECTIVE VENTED ORANGE SHIRT</h5><div class="cat">Furniture</div><div class="price">$44.95</div></div>
<div class="product abs" style="left:883px;top:1411px"><div class="img" style="height:247px" role="img" aria-label="Orange standard vented shirt"><i style="background:#f6741a;width:140px;height:160px"></i></div><h5>MENS L/S STANDARD VENTED ORANGE SHIRT</h5><div class="cat">Accessories</div><div class="price">$43.95</div></div>

<!-- product row 2 -->
<div class="product abs" style="left:85px;top:1827px"><div class="img" role="img" aria-label="Hi-vis polo shirts in yellow and orange"><i style="background:linear-gradient(90deg,#c9f05a 50%,#f27a1a 50%)"></i></div><h5>HI- VIS L/S POLO</h5><div class="cat">Furniture</div><div class="price">$23.00</div></div>
<div class="product abs" style="left:351px;top:1827px"><div class="img" role="img" aria-label="Navy work pants with reflective tape"><i style="background:#1f2d5a;width:90px"></i><span class="badge" style="background:#e53512">HOT</span></div><span class="rating">4 <span style="color:#f5b400">★</span></span><h5>HI-VIS NAVY PANTS - DOUBLE HOOP</h5><div class="cat">Accessories</div><div class="price">$47.00</div></div>
<div class="product abs" style="left:617px;top:1827px"><div class="img" role="img" aria-label="Orange reflective vented shirt"><i style="background:#f37a1e;width:190px"></i><span class="badge" style="background:var(--green)">NEW</span></div><h5>MENS L/S REFLECTIVE VENTED ORANGE SHIRT</h5><div class="cat">Furniture</div><div class="price">$44.95</div></div>
<div class="product abs" style="left:884px;top:1827px"><div class="img" style="height:247px" role="img" aria-label="Orange standard vented shirt"><i style="background:#f6741a;width:140px;height:160px"></i></div><h5>MENS L/S STANDARD VENTED ORANGE SHIRT</h5><div class="cat">Accessories</div><div class="price">$43.95</div></div>

<section class="brands-band abs">
  <h2 class="section-title abs" style="top:76px">POPULAR<em>BRANDS</em></h2>
  <div class="arrow-dot abs" style="left:110px;top:203px"></div>
  <div class="brand abs" style="left:218px;top:200px">NORVIK</div>
  <div class="brand abs" style="left:392px;top:200px;display:flex;gap:8px;align-items:center"><span style="width:24px;height:24px;border-radius:50%;background:#1d3d5e;display:inline-block"></span>PELLAM</div>
  <div class="brand abs" style="left:562px;top:200px">HALDEN</div>
  <div class="brand abs" style="left:742px;top:200px">STEPCRAFT</div>
  <div class="brand abs" style="left:912px;top:200px">VELTRA</div>
  <div class="arrow-dot abs" style="left:1090px;top:203px"></div>
</section>

<h2 class="abs" style="left:68px;top:2660px;font-size:44px;font-weight:700">LATEST <span style="color:var(--orange);margin-left:12px">NEWS</span></h2>
<div class="btn btn-orange abs" style="left:945px;top:2663px;width:180px;height:45px">VIEW ALL <span>⟶</span></div>

<article class="news-card abs" style="left:60px;top:2760px" role="img" aria-label="Chainsaw cutting wood with sawdust"><div class="date">27<small>AUG</small></div><div class="news-meta"><span class="tag">DECORATION</span><h5>Exploring Atlanta’s modern homes</h5><small>Admin · 0 · share</small></div></article>
<article class="news-card abs" style="left:335px;top:2760px" role="img" aria-label="Worker using a power saw"><div class="date">27<small>AUG</small></div><div class="news-meta"><span class="tag">INSPIRATION</span><h5>Green interior design inspiration</h5><small>Admin · 0 · share</small></div></article>
<article class="news-card abs" style="left:610px;top:2760px;background:linear-gradient(160deg,#5a8ccf,#2d5590)" role="img" aria-label="Worker climbing scaffolding under blue sky"><div class="date">27<small>AUG</small></div><div class="news-meta"><span class="tag">FURNITURE</span><h5>Collar brings back coffee brewing ritual</h5><small>Admin · 0 · share</small></div></article>
<article class="news-card abs" style="left:885px;top:2760px" role="img" aria-label="Welder at work on a steel frame"><div class="date">27<small>AUG</small></div><div class="news-meta"><span class="tag">DESIGN TRENDS</span><h5>Reinterprets the classic bookshelf</h5><small>Admin · 0 · share</small></div></article>

<section class="newsletter abs">
  <h2 class="abs">GET NEWS AND<br>OFFERS FIRST!</h2>
  <div class="field abs">EMAIL ADDRESS</div>
  <div class="btn btn-dark abs">SUBSCRIBE NOW <span>⟶</span></div>
</section>
<div class="abs" style="left:955px;top:3180px;width:185px;height:290px;background:linear-gradient(180deg,#f28a2a,#f7b34a);border-radius:90px 90px 0 0" role="img" aria-label="Worker in orange hard hat and hi-vis vest with arms crossed"></div>

<footer class="footer abs">
  <div class="abs wordmark" style="left:12px;top:28px;font-size:31px">IRONLINE<small style="color:#fff">WORKGEAR</small></div>
  <p class="about abs" style="left:10px;top:86px;width:270px">Condimentum adipiscing vel neque dis nam parturient orci at scelerisque neque dis nam parturient.</p>
  <div class="contact abs" style="left:10px;top:166px">
    <div>➤&nbsp; 28 Harrow Lane, UK, Leeds</div>
    <div>▯&nbsp; Phone: (010) 555-0142</div>
    <div>✉&nbsp; Fax: (010) 555-0199</div>
  </div>
  <div class="abs" style="left:312px;top:48px"><h6>RECENT POSTS</h6>
    <div class="post" style="margin-top:22px"><i></i><div>Exploring Atlanta’s modern<br>homes<small>August 27, 2021 &nbsp;No Comments</small></div></div>
    <div class="post" style="margin-top:30px"><i></i><div>Green interior design<br>inspiration<small>August 27, 2021 &nbsp;No Comments</small></div></div>
  </div>
  <div class="abs" style="left:616px;top:48px"><h6>OUR STORES</h6><ul><li>New York</li><li>London SF</li><li>Edinburgh</li><li>Los Angeles</li><li>Chicago</li><li>Las Vegas</li></ul></div>
  <div class="abs" style="left:818px;top:48px"><h6>USEFUL LINKS</h6><ul><li>Privacy Policy</li><li>Returns</li><li>Terms &amp; Conditions</li><li>Contact Us</li><li>Latest News</li><li>Our Sitemap</li></ul></div>
  <div class="abs" style="left:1020px;top:48px"><h6>FOOTER MENU</h6><ul><li>Instagram profile</li><li>New Collection</li><li>Woman Dress</li><li>Contact Us</li><li>Latest News</li><li>Purchase Theme</li></ul></div>
  <div class="abs" style="left:0;top:302px;width:1200px;height:1px;background:#222"></div>
  <div class="abs" style="left:948px;top:325px;display:flex;gap:8px">
    <span class="pay">CARD A</span><span class="pay">CARD B</span><span class="pay">CARD C</span><span class="pay">CARD D</span><span class="pay">CARD E</span>
  </div>
  <div class="abs" style="left:1140px;top:290px;width:50px;height:50px;border-radius:50%;background:#fff;display:flex;align-items:center;justify-content:center"><svg width="16" height="10" viewBox="0 0 16 10"><path d="M1 9l7-7 7 7" fill="none" stroke="#f25c05" stroke-width="2"/></svg></div>
</footer>

</body>
</html>
```